International Sustainable Cities NGO needs PPT Design

We need a PPT design for a presentation upcoming at a leading university on the East coast. The design needs to be clean and simple, professional and room for photos and maps. It's a presentation about citizen mapping and data collection for city planning/decision making.

University

```html
<!DOCTYPE html>
<html lang="en">
<head>
<meta charset="UTF-8">
<title>Greenward Collective – Slide 7</title>
<link href="https://fonts.googleapis.com/css2?family=Source+Sans+3:wght@400;500&family=Cinzel:wght@400&display=swap" rel="stylesheet">
<style>
  :root {
    --bar-green: #579f56;
    --brand-green: #0f4c3a;
    --accent-green: #4b9a45;
    --ink: #1b1b1b;
    --rule: #d2d2d2;
    --ghost: #eef2f0;
    --paper: #ffffff;
  }
  * { margin: 0; padding: 0; box-sizing: border-box; }
  html, body { width: 1200px; height: 757px; overflow: hidden; background: var(--paper); }
  .slide {
    position: relative;
    width: 1200px;
    height: 757px;
    overflow: hidden;
    background: var(--paper);
    font-family: "Source Sans 3", "Myriad Pro", sans-serif;
  }
  .top-bar {
    position: absolute; left: 0; top: 0;
    width: 100%; height: 19px;
    background: var(--bar-green);
  }
  .brand {
    position: absolute; left: 0; top: 52px; width: 100%;
    text-align: center;
    font-family: "Cinzel", "Trajan Pro", serif;
    color: var(--brand-green);
    line-height: 1;
  }
  .brand-line { display: block; font-size: 30px; letter-spacing: 7px; }
  .brand-line + .brand-line { margin-top: 12px; font-size: 27px; letter-spacing: 8px; }
  .body-copy {
    position: absolute; left: 80px; top: 215px; width: 1080px;
    font-size: 15.6px; line-height: 27px; color: var(--ink);
  }
  .body-copy .line { display: block; white-space: nowrap; }
  .body-copy .highlight { color: var(--accent-green); }
  .divider {
    position: absolute; left: 111px; top: 526px;
    width: 979px; height: 1px; background: var(--rule);
  }
  .closing-copy { top: 540px; }
  .page-number {
    position: absolute; left: 589px; top: 698px;
    width: 23px; height: 23px;
    border: 1.3px solid var(--ink); border-radius: 50%;
    font-size: 12px; line-height: 20px; text-align: center;
    color: var(--accent-green);
  }
  .ghost-brand {
    position: absolute; left: 858px; top: 628px;
    font-family: "Cinzel", "Trajan Pro", serif;
    color: var(--ghost); line-height: 1; white-space: nowrap;
  }
  .ghost-brand span { display: block; font-size: 62px; letter-spacing: 14px; }
  .ghost-brand span + span { margin-top: 20px; font-size: 56px; letter-spacing: 16px; }
</style>
</head>
<body>
<main class="slide">
  <div class="top-bar"></div>

  <div class="ghost-brand" aria-hidden="true">
    <span>GREENWARD</span>
    <span>COLLECTIVE</span>
  </div>

  <header class="brand">
    <span class="brand-line">GREENWARD</span>
    <span class="brand-line">COLLECTIVE</span>
  </header>

  <section class="body-copy">
    <span class="line">Lorem ipsum dolor sit amet, consectetur adipisicing elit, sed do eiusmod tempor incididunt ut labore et dolore magna aliqua.</span>
    <span class="line">&nbsp;Ut enim ad minim veniam, quis nostrud exercitation ullamco laboris nisi ut aliquip ex ea commodo consequat. Duis aute irure dolor in reprehende-</span>
    <span class="line">rit in voluptate velit esse cillum dolore eu fugiat nulla pariatur. Excepteur sint occaecat cupidatat non proident, sunt in culpa qui officia deserunt</span>
    <span class="line">mollit anim id est laborum. Sed ut perspiciatis unde omnis iste natus error sit voluptatem accusantium doloremque laudantium, totam rem ape-</span>
    <span class="line">riam, eaque ipsa quae ab illo inventore veritatis et quasi architecto</span>
    <span class="line highlight">beatae vitae dicta sunt explicabo. Nemo enim ipsam voluptatem quia voluptas sit aspernatur aut odit aut fugit, sed quia consequuntur magni do-</span>
    <span class="line highlight">lores eos qui ratione voluptatem sequi nesciunt. Neque porro quisquam est, qui dolorem ipsum quia dolor sit amet, consectetur, adipisci velit, sed</span>
    <span class="line highlight">quia non numquam eius modi tempora incidunt ut labore et dolore magnam aliquam quaerat voluptatem.</span>
    <span class="line">Excepteur sint occaecat cupidatat non proident, sunt in culpa qui officia deserunt mollit anim id est laborum. Sed ut perspiciatis unde omnis iste</span>
    <span class="line">natus error sit voluptatem accusantium doloremque laudantium, totam rem aperiam, eaque ipsa quae ab illo inventore veritatis et quasi architecto</span>
    <span class="line">Duis aute irure dolor in reprehenderit in voluptate velit esse cillum dolore eu fugiat nulla pariatur.</span>
  </section>

  <div class="divider"></div>

  <section class="body-copy closing-copy">
    <span class="line">Excepteur sint occaecat cupidatat non proident, sunt in culpa qui officia deserunt mollit anim id est laborum. Sed ut perspiciatis unde omnis iste</span>
    <span class="line">natus error sit voluptatem accusantium doloremque laudantium, totam rem aperiam, eaque ipsa quae ab illo inventore veritatis et quasi architecto</span>
  </section>

  <div class="page-number">7</div>
</main>
</body>
</html>
```